Become a real French Pastry chef with an easy 3 step pastry kit box.

The company is specialized in French pastries and the boxes will be sold online, and retail stores. The goal is for anyone who likes to be creative and crafty to create and bake their own traditional french pastry in 3 easy steps right at home. French pastries can be known to take hours to bake. These boxes allow you to make them very quickly, no hassle and they results taste amazing. All the ingredients are from FRANCE. Everything you need is in the box, All you need is water! The box design desired is elegant, simple, glamorous but yet eye catchy for retail distribution. This is a kit box with pre scaled ingredients to make your own eclairs. Box dimensions are 8x6x2.
Updates

Target Market(s)

Middle Aged, middle to upper class housewives who enjoy cooking and baking

Industry/Entity Type

Bakery

Font styles to use
Decorative
Script

Colors

Designer to choose colors to be used in the design.

Requirements
Must have
• This box will be called "The Choux Kit by {logo}, or {logo} presents The Choux Kit.
• Has to have the instructions (attached document)
• "This box contains: 4 éclair shells, powder pouch, icing bag, pipping bag and pipping tip"
• Net weight 245g
• Nutrition label (attached)
Nice to have
• An eclair on it.

```html
<!DOCTYPE html>
<html lang="en">
<head>
<meta charset="utf-8">
<title>The Choux Kit – Box Dieline</title>
<link rel="stylesheet" href="https://fonts.googleapis.com/css2?family=Lobster&family=Courgette&family=Open+Sans:wght@400;600&family=Arimo:wght@400;700&display=swap">
<style>
  :root {
    --bg: #000000;
    --board: #ffffff;
    --kraft: #bdae79;
    --lid-teal: #4ecdcb;
    --ring-pale: #bfeeed;
    --ring-magenta: #c9338f;
    --base-blue: #55bff6;
    --choc: #5a1c0e;
    --accent-red: #d3232a;
    --logo-blue: #2a57c9;
    --ink: #111111;
    --white: #ffffff;
  }
  * { box-sizing: border-box; margin: 0; padding: 0; }
  html, body { width: 1200px; height: 1200px; overflow: hidden; background: var(--bg); }
  .canvas { position: relative; width: 1200px; height: 1200px; background: var(--bg); }
  .dieline { position: absolute; inset: 0; }
  .panel { position: absolute; }

  .lid { left: 376px; top: 176px; width: 462px; height: 350px; background: var(--lid-teal); }
  .badge-ring { position: absolute; left: 66px; top: 6px; width: 340px; height: 340px; border-radius: 50%; background: var(--ring-pale); }
  .badge-core { position: absolute; left: 98px; top: 38px; width: 276px; height: 276px; border-radius: 50%; background: var(--white); border: 2px solid var(--ring-magenta); overflow: hidden; }
  .brand { position: absolute; left: 0; right: 0; top: 40px; text-align: center; font-family: "Courgette", cursive; font-size: 22px; line-height: 26px; color: var(--logo-blue); }
  .brand-dot { display: block; width: 12px; height: 12px; border-radius: 50%; background: var(--ring-magenta); margin: 0 auto 8px; }
  .presents { position: absolute; left: 0; right: 0; top: 120px; text-align: center; font-family: "Courgette", cursive; font-size: 14px; line-height: 18px; color: var(--accent-red); }
  .kit-title { position: absolute; left: 0; right: 0; top: 138px; text-align: center; font-family: "Lobster", cursive; font-weight: 400; font-size: 38px; line-height: 46px; color: var(--choc); }
  .eclair-photo { position: absolute; left: 94px; top: 190px; width: 112px; height: 64px; border-radius: 28px; background: linear-gradient(160deg, #2a140c 0%, #5b2d16 45%, #d8a85e 100%); }

  .front { left: 366px; top: 526px; width: 484px; height: 146px; background: var(--kraft); }
  .nutrition { position: absolute; left: 6px; top: 20px; width: 472px; height: 78px; background: var(--white); border: 1px solid var(--ink); padding: 3px 4px; display: flex; gap: 6px; font-family: "Arimo", sans-serif; color: var(--ink); font-size: 5px; line-height: 1.4; overflow: hidden; }
  .nf-head { width: 80px; }
  .nf-title { font-weight: 700; font-size: 13px; line-height: 0.95; }
  .nf-col { flex: 1; border-top: 3px solid var(--ink); }
  .nf-row { display: flex; justify-content: space-between; border-bottom: 0.5px solid #888; }
  .nf-row.sub { padding-left: 8px; }
  .nf-vit { white-space: nowrap; font-size: 4.5px; margin-top: 2px; }
  .nf-foot { width: 112px; font-size: 4px; line-height: 1.4; }
  .contents { position: absolute; left: 10px; top: 104px; font-family: "Arimo", sans-serif; font-size: 9.5px; color: var(--white); line-height: 14px; }

  .base { left: 365px; top: 672px; width: 488px; height: 348px; background: var(--base-blue); color: var(--white); font-family: "Open Sans", sans-serif; text-align: center; }
  .step-title { font-size: 13px; font-weight: 400; line-height: 17px; margin-top: 12px; }
  .base .step-title:first-child { margin-top: 16px; }
  .step-text { font-size: 12.5px; line-height: 17px; padding: 4px 6px 0; }
  .ingredients { position: absolute; left: 15px; top: 242px; width: 320px; text-align: left; font-size: 8px; line-height: 11.5px; }
</style>
</head>
<body>
<main class="canvas">
  <svg class="dieline" width="1200" height="1200" viewBox="0 0 1200 1200" aria-hidden="true">
    <rect x="366" y="30" width="484" height="146" fill="var(--board)"/>
    <path d="M366 30 H330 Q250 40 232 145 V164 Q232 172 242 172 H366 Z" fill="var(--kraft)"/>
    <path d="M850 30 H886 Q966 40 984 145 V164 Q984 172 974 172 H850 Z" fill="var(--kraft)"/>
    <rect x="232" y="178" width="150" height="348" rx="16" fill="var(--board)"/>
    <rect x="832" y="178" width="152" height="348" rx="16" fill="var(--board)"/>
    <rect x="196" y="528" width="176" height="140" rx="8" fill="var(--kraft)"/>
    <rect x="844" y="528" width="176" height="140" rx="8" fill="var(--kraft)"/>
    <rect x="61" y="674" width="310" height="344" rx="8" fill="var(--board)"/>
    <rect x="848" y="674" width="308" height="344" rx="8" fill="var(--board)"/>
    <rect x="196" y="1020" width="176" height="144" rx="8" fill="var(--kraft)"/>
    <rect x="834" y="1020" width="184" height="144" rx="8" fill="var(--kraft)"/>
    <rect x="366" y="1020" width="474" height="144" fill="var(--board)"/>
  </svg>

  <section class="panel lid">
    <div class="badge-ring" role="img" aria-label="Circular badge border with a teal dot and triangle pattern"></div>
    <div class="badge-core">
      <div class="brand"><span class="brand-dot"></span>Maison Doucette</div>
      <div class="presents">Presents</div>
      <h1 class="kit-title">The Choux Kit</h1>
      <div class="eclair-photo" role="img" aria-label="Photo of two chocolate glazed eclairs"></div>
    </div>
  </section>

  <section class="panel front">
    <div class="nutrition">
      <div class="nf-head">
        <div class="nf-title">Nutrition<br>Facts</div>
        <div>Serving Size 1 éclair (100g)</div>
        <div>Servings Per Container 4</div>
        <div><b>Calories</b> 262</div>
      </div>
      <div class="nf-col">
        <div class="nf-row"><b>Amount Per Serving</b><b>% Daily Value*</b></div>
        <div class="nf-row"><span><b>Total Fat</b> 16g</span><b>25%</b></div>
        <div class="nf-row sub"><span>Saturated Fat 4.1g</span><b>21%</b></div>
        <div class="nf-row sub"><span>Trans Fat 0g</span><span></span></div>
        <div class="nf-row sub"><span>Polyunsaturated Fat 3.9g</span><span></span></div>
        <div class="nf-row sub"><span>Monounsaturated Fat 6g</span><span></span></div>
        <div class="nf-row"><span><b>Cholesterol</b> 127mg</span><b>42%</b></div>
        <div class="nf-vit">Vitamin A 16% • Calcium 6% • Vitamin B6 5% • Vitamin B12 5%</div>
      </div>
      <div class="nf-col">
        <div class="nf-row"><b>Amount Per Serving</b><b>% Daily Value*</b></div>
        <div class="nf-row"><span><b>Potassium</b> 3mg</span><b>0%</b></div>
        <div class="nf-row"><span><b>Sodium</b> 337mg</span><b>14%</b></div>
        <div class="nf-row"><span><b>Total Carbohydrate</b> 24g</span><b>8%</b></div>
        <div class="nf-row sub"><span>Dietary Fiber 0.6g</span><b>2%</b></div>
        <div class="nf-row sub"><span>Sugars 7g</span><span></span></div>
        <div class="nf-row"><span><b>Protein</b> 6g</span><b>12%</b></div>
        <div class="nf-vit">Iron 6% • Magnesium 3% • Vitamin D 9%</div>
      </div>
      <div class="nf-foot">
        *Percent Daily Values are based on a 2,000 calorie diet. Your daily values may be higher or lower depending on your calorie needs.<br>
        Total Fat less than 65g / 80g<br>Sat Fat less than 20g / 25g<br>Cholesterol less than 300mg<br>Sodium less than 2400mg<br>Total Carbs 300g / 375g<br>Dietary Fiber 25g / 30g
      </div>
    </div>
    <div class="contents">
      This Box Contains :<br>
      4 éclair shells • powder pouch • icing bag • pipping bag • pipping tip<br>
      Net weight 245g
    </div>
  </section>

  <section class="panel base">
    <h2 class="step-title">Step 1</h2>
    <p class="step-text">Mix powder patch with 1 cup of cold water, mix for 2 minutes on high speed.<br>Let the custard rest in fridge for 15 minutes</p>
    <h2 class="step-title">Step 2</h2>
    <p class="step-text">Place pipping tip in pipping bag. Poor custard in bag before cutting the tip off of it off. Pipe custard inside eclair by slightly pressing on flat side of the shell in 3 separate areas for a more uniform filling. Do not over fill or shell will crack.</p>
    <h2 class="step-title">Step 3</h2>
    <p class="step-text">Place icing in warm water for 2 minutes, cut bag at an angle, then poor on<br>top of eclair</p>
    <div class="ingredients">
      Ingredients :<br>
      Eclair shell: wheat flour(gluten), butter fat 26%, egg, water, potassium and sodium diphosphates, sodium carbonates, salt, sorbitol.<br>
      Powder: sugar, modified potato starch(E 1414), whole milk powder, lactose and milk proteins, thickeners : calcium lactate, disodium phosphate, disodium diphosphate, sodium alginate, carrageenan, artificial and natural flavors: vanillin, caramel, colors: E 102, E 110 (may contain cocoa powder)<br>
      Icing: sugar, glucose syrup, water (may contain cocoa powder)
    </div>
  </section>
</main>
</body>
</html>
```